TITLE: Business Card Template

NEEDED
I need a business card template that is based on the style of this brochure.

ATTACHMENTS
See link to file : https://files.quellora-share.net/u/58302714/Brochure.pdf

GUIDELINES

STYLE - Please see the following guidelines, but PLEASE BE CREATIVE

- See attached brochure that we have used to see the style that must be replicated in some form or another
- The Text MUST be Tahoma / Veranda.
- You must use the colors of the Brochure

Target audience for the video:
- Gallery owner / Art Dealer
- High net worth / High income
- Sophisticated, major city dweller
- Age 40-60

CONTENT – We need the space for the following (two sided):
FRONT:
Name
Title
Address - street
Address -city, postal code
Address - country
Phone
Email

BACK:
Company Logo
Company website
Phone - main number

OUTPUT / DELIVERABLE – we will need source files for the card.

NOTES:

We also have lots of ongoing work and tend to work with vendors again and again. So consider this project as sort of an "interview."

```html
<!DOCTYPE html>
<html lang="en">
<head>
<meta charset="utf-8">
<title>The Gallerist's Lens – Business Card</title>
<link href="https://fonts.googleapis.com/css2?family=PT+Sans:wght@400;700&display=swap" rel="stylesheet">
<style>
  :root {
    --page: #e9e6df;
    --slate-top: #5d6576;
    --slate-bottom: #434a59;
    --gold: #cbb98c;
    --gold-dark: #b39f6c;
    --gold-text: #c9b37a;
    --ink-light: #e4e6ea;
    --ink-soft: #c3c7cf;
    --rule: #8a8f9a;
  }
  * { margin: 0; padding: 0; box-sizing: border-box; }
  html, body { width: 1200px; height: 800px; overflow: hidden; }
  body {
    background: var(--page);
    font-family: "PT Sans", Tahoma, Verdana, sans-serif;
    position: relative;
  }
  .card {
    position: absolute;
    width: 600px;
    height: 340px;
    background: linear-gradient(160deg, var(--slate-top), var(--slate-bottom));
    overflow: hidden;
    box-shadow: 0 6px 18px rgba(0,0,0,0.18);
  }
  .card--back { left: 80px; top: 60px; }
  .card--front { left: 520px; top: 410px; }

  .brand {
    position: absolute;
    color: var(--ink-light);
    font-weight: 400;
    line-height: 1;
    white-space: nowrap;
  }
  .brand sup { font-size: 0.35em; vertical-align: 1.4em; margin-left: 2px; }

  .card--back .brand { left: 48px; top: 128px; font-size: 52px; }

  .band {
    position: absolute;
    left: 0; right: 0; bottom: 0;
    background: linear-gradient(180deg, var(--gold), var(--gold-dark));
  }
  .card--back .band { height: 34px; }
  .band__phone {
    position: absolute;
    left: 24px; top: 8px;
    font-size: 14px; font-weight: 700;
    color: #fff;
    letter-spacing: 0.5px;
  }
  .card--back .website {
    position: absolute;
    right: 22px; bottom: 44px;
    font-size: 14px;
    color: var(--ink-soft);
  }

  .card--front .brand { left: 40px; top: 56px; font-size: 46px; }
  .card--front .rule {
    position: absolute;
    left: 40px; top: 128px;
    width: 300px; height: 1px;
    background: var(--rule);
  }
  .card--front .band { height: 18px; }

  .person {
    position: absolute;
    right: 30px; top: 112px;
    text-align: right;
  }
  .person__name {
    color: var(--gold-text);
    font-weight: 700;
    font-size: 17px;
    letter-spacing: 1px;
    text-transform: uppercase;
  }
  .person__title { color: var(--ink-soft); font-size: 13px; margin-top: 2px; }
  .person__pin { display: block; margin: 8px 0 6px auto; }
  .person__address { color: var(--ink-soft); font-size: 13px; line-height: 1.35; }

  .contact {
    position: absolute;
    left: 40px; bottom: 32px;
    color: var(--ink-soft);
    font-size: 13px;
    line-height: 1.4;
  }
  .contact__row { display: flex; align-items: center; gap: 7px; }
  .contact__row svg { flex: none; }
</style>
</head>
<body>

  <section class="card card--back" aria-label="Card back">
    <div class="brand">The Gallerist's Lens<sup>TM</sup></div>
    <div class="website">www.GalleristsLens.com</div>
    <div class="band">
      <span class="band__phone">+1 888-555-0142</span>
    </div>
  </section>

  <section class="card card--front" aria-label="Card front">
    <div class="brand">The Gallerist's Lens<sup>TM</sup></div>
    <div class="rule"></div>

    <div class="person">
      <div class="person__name">Daniel Whitford</div>
      <div class="person__title">Executive Director</div>
      <svg class="person__pin" width="12" height="16" viewBox="0 0 12 16" aria-hidden="true">
        <path d="M6 1a5 5 0 0 0-5 5c0 3.6 5 9 5 9s5-5.4 5-9a5 5 0 0 0-5-5z" fill="none" stroke="#c9b37a" stroke-width="1.5"/>
        <circle cx="6" cy="6" r="1.8" fill="#c9b37a"/>
      </svg>
      <div class="person__address">
        48 Harlow Lane<br>
        Brookfield, Vermont 05036<br>
        United States
      </div>
    </div>

    <div class="contact">
      <div>P.O. Box 318</div>
      <div>Fairlee, Vermont 05045</div>
      <div class="contact__row">
        <svg width="12" height="12" viewBox="0 0 12 12" aria-hidden="true">
          <path d="M1 3c0-1 .8-1.6 1.6-1.6h6.8C10.2 1.4 11 2 11 3v1H8.5V3h-5v1H1z" fill="#c9b37a"/>
          <rect x="2" y="5" width="8" height="6" rx="1" fill="#c9b37a"/>
        </svg>
        <span>+1 888-555-0142</span>
      </div>
      <div class="contact__row">
        <svg width="12" height="10" viewBox="0 0 12 10" aria-hidden="true">
          <rect x="0.5" y="0.5" width="11" height="9" fill="#c9b37a"/>
          <path d="M0.5 0.5 6 5.5 11.5 0.5" fill="none" stroke="#434a59" stroke-width="1"/>
        </svg>
        <span>hello@galleristslens.com</span>
      </div>
    </div>

    <div class="band"></div>
  </section>

</body>
</html>
```